Vexo App Form Input Screens - Sleek Clean Design

We have a input form that we would like to transpose into an Vexo App. We have a programmer to do the screens but we need to take this very field heavy form and get it into clean design input screens (We can as many screens as make sense). We want to design to be slick and intuitive. This will be used by young guys who enjoy a gaming atmosphere. But the design has to be easy enough to be completely intuitive to a novice user. The Company likes to do things with Sky Blue colors. Also OK to incorporate burnt orange/yellow (Think glowing sun).

Target Market(s)

18-25 year old males - These guys go door to door and input this data all day

Industry/Entity Type

Solar Energy

Number of Pages Required

5+ page

Font styles to use
Sans Serif

Colors
0355a3
3277b5
85acd3
d0dfed
faa54b
ffc214
f68e4d

Requirements
Must have
• Clean simple sleek Designs - Drop Down Examples. The background and fields have to have distinct colors because these guys will be outside most of the time and if the design is not contrasted enough, it will be hard for them to see.
Nice to have
• Fun ways to incorporate the Glowing Sun Colors (Subtle)
Should not have
• Should not look like Powerpoint

```html
<!DOCTYPE html>
<html lang="en">
<head>
<meta charset="utf-8">
<title>Solvia – Site Survey Form</title>
<link href="https://fonts.googleapis.com/css2?family=Open+Sans:wght@400;600;700&family=Raleway:wght@500;600&display=swap" rel="stylesheet">
<style>
:root{
  --brand-deep:#0355a3;
  --brand-mid:#0b6fc4;
  --brand-soft:#85acd3;
  --table-head:#0b4d9c;
  --heading:#0355a3;
  --label:#555b63;
  --field-bg:#e9eef4;
  --field-border:#a9b8c9;
  --placeholder:#7a828c;
  --divider:#d0dfed;
  --grid:#b9c6d4;
  --footer-bg:#f4f6f8;
  --sun-1:#faa54b;
  --sun-2:#ffc214;
  --sun-3:#f68e4d;
  --white:#ffffff;
}
*{box-sizing:border-box;margin:0;padding:0}
html,body{width:1200px;height:1107px;overflow:hidden;background:var(--white)}
.stage{position:absolute;left:0;top:0;width:1366px;height:1260px;transform:scale(0.8785);transform-origin:0 0;font-family:"Open Sans",sans-serif;color:var(--label);font-size:12.5px}
.stage>*{position:absolute}
.top-bar{left:0;top:0;width:1366px;height:113px;background:linear-gradient(180deg,var(--brand-mid) 0%,var(--brand-deep) 100%)}
.sun-rule{left:0;top:113px;width:1366px;height:3px;background:linear-gradient(90deg,var(--sun-3),var(--sun-2) 50%,var(--sun-1))}
.brand-name{left:155px;top:24px;font-weight:700;font-size:48px;line-height:60px;color:var(--white)}
.section-title{font-family:"Raleway",sans-serif;font-weight:600;font-size:14px;color:var(--heading);letter-spacing:.2px;line-height:18px}
.label{font-size:12.5px;color:var(--label);white-space:nowrap;line-height:16px}
.field{height:26px;background:var(--field-bg);border:1px solid var(--field-border);border-radius:2px;font-size:12.5px;color:var(--placeholder);padding:0 10px;line-height:24px}
.select{height:26px;background:var(--field-bg);border:1px solid var(--field-border);border-radius:2px;font-size:11px;color:var(--label);padding:0 10px;line-height:24px}
.select svg{position:absolute;right:9px;top:8px}
.radio{width:18px;height:18px;border-radius:50%;border:1px solid var(--field-border);background:var(--field-bg)}
.note{font-size:10.5px;color:var(--label);line-height:14px;white-space:nowrap}
.divider{left:160px;top:656px;width:510px;height:3px;background:var(--divider)}
.survey-table{left:740px;top:452px;width:468px;border-collapse:collapse;font-size:12.5px}
.survey-table th{background:var(--table-head);color:var(--white);font-weight:400;height:35px;font-size:12.5px;border-right:1px solid #3d73b3;white-space:nowrap}
.survey-table th.group{text-align:left;padding-left:17px;font-family:"Raleway",sans-serif;font-weight:500;font-size:14px}
.survey-table td{height:31.5px;border:1px solid var(--grid);background:var(--field-bg)}
.survey-table td.row-label{background:var(--white);padding-left:19px;color:var(--label);white-space:nowrap}
.survey-table td.row-label.strong{color:#2c3138;font-weight:600}
.footer{left:0;top:1195px;width:1366px;height:65px;background:var(--footer-bg);border-top:1px solid var(--divider)}
.copyright{left:162px;top:1223px;font-size:12.5px;color:var(--label)}
</style>
</head>
<body>
<div class="stage">
  <header class="top-bar"></header>
  <div class="sun-rule"></div>
  <div class="brand-name">Solvia</div>

  <h2 class="section-title" style="left:158px;top:158px">RECORD TYPE</h2>
  <span class="radio" style="left:160px;top:188px"></span><span class="label" style="left:184px;top:188px">Brightwave</span>
  <span class="radio" style="left:263px;top:188px"></span><span class="label" style="left:288px;top:188px">RayPath</span>
  <span class="radio" style="left:363px;top:188px"></span><span class="label" style="left:385px;top:188px">TopRidge</span>
  <span class="radio" style="left:459px;top:188px"></span><span class="label" style="left:482px;top:188px">Cash</span>
  <span class="label" style="left:530px;top:188px">Other</span>
  <div class="field" style="left:573px;top:183px;width:95px"></div>

  <h2 class="section-title" style="left:158px;top:226px">CUSTOMER INFORMATION</h2>
  <span class="label" style="left:160px;top:259px">Who Passed Credit?</span>
  <div class="field" style="left:373px;top:254px;width:152px"></div>
  <p class="note" style="left:536px;top:250px">(For RayPath, this person<br>must be on title)</p>
  <span class="label" style="left:160px;top:290px">Name as it Appears on Electric Bill</span>
  <div class="field" style="left:373px;top:285px;width:296px"></div>
  <span class="label" style="left:160px;top:322px">Primary Owner (Full Name)</span>
  <div class="field" style="left:373px;top:318px;width:197px"></div>
  <div class="select" style="left:576px;top:319px;width:93px">On Tittle<svg width="12" height="8" viewBox="0 0 12 8"><path d="M1 1l5 5 5-5" fill="none" stroke="#444" stroke-width="1.4"/></svg></div>
  <span class="label" style="left:160px;top:353px">Email</span>
  <div class="field" style="left:373px;top:350px;width:296px"></div>
  <span class="label" style="left:160px;top:384px">Home Phone</span>
  <div class="field" style="left:373px;top:381px;width:296px"></div>
  <span class="label" style="left:160px;top:416px">Cell Phone</span>
  <div class="field" style="left:373px;top:413px;width:296px"></div>

  <h2 class="section-title" style="left:160px;top:474px">SECONDARY CUSTOMER INFORMATION</h2>
  <span class="label" style="left:161px;top:505px">Secondary Owner (Full Name)</span>
  <div class="field" style="left:373px;top:507px;width:196px"></div>
  <div class="select" style="left:575px;top:507px;width:94px">On Tittle<svg width="12" height="8" viewBox="0 0 12 8"><path d="M1 1l5 5 5-5" fill="none" stroke="#444" stroke-width="1.4"/></svg></div>
  <span class="label" style="left:161px;top:536px">Email</span>
  <div class="field" style="left:373px;top:538px;width:296px"></div>
  <span class="label" style="left:161px;top:568px">Home Phone</span>
  <div class="field" style="left:373px;top:572px;width:296px"></div>
  <span class="label" style="left:161px;top:599px">Cell Phone</span>
  <div class="field" style="left:373px;top:603px;width:296px"></div>

  <div class="divider"></div>

  <span class="label" style="left:162px;top:693px">Installation Address</span>
  <div class="field" style="left:373px;top:688px;width:296px"></div>
  <span class="label" style="left:162px;top:725px">City</span>
  <div class="field" style="left:373px;top:719px;width:95px"></div>
  <div class="field" style="left:475px;top:719px;width:94px">State</div>
  <div class="field" style="left:574px;top:719px;width:95px">Zip</div>
  <span class="label" style="left:162px;top:756px">Township Taxes Paid to</span>
  <div class="field" style="left:373px;top:752px;width:296px"></div>
  <span class="label" style="left:162px;top:788px">Does Customer have HOA?</span>
  <div class="select" style="left:373px;top:784px;width:148px">Choose<svg width="12" height="8" viewBox="0 0 12 8"><path d="M1 1l5 5 5-5" fill="none" stroke="#444" stroke-width="1.4"/></svg></div>
  <div class="field" style="left:526px;top:784px;width:143px">Name</div>
  <span class="label" style="left:162px;top:819px">HOA Address</span>
  <div class="field" style="left:374px;top:816px;width:172px"></div>
  <div class="field" style="left:551px;top:816px;width:118px">Phone</div>

  <h2 class="section-title" style="left:160px;top:882px">UTILITY INFORMATION</h2>
  <span class="label" style="left:160px;top:920px">Utility</span>
  <div class="field" style="left:199px;top:915px;width:118px"></div>
  <span class="label" style="left:324px;top:920px">Account</span>
  <div class="field" style="left:375px;top:915px;width:119px"></div>
  <span class="label" style="left:506px;top:920px">Meter</span>
  <div class="field" style="left:547px;top:915px;width:118px"></div>
  <span class="label" style="left:160px;top:955px">Usage (yearly)</span>
  <div class="field" style="left:256px;top:950px;width:151px"></div>
  <span class="label" style="left:418px;top:954px">Meter Location</span>
  <div class="select" style="left:514px;top:950px;width:152px">Choose<svg width="12" height="8" viewBox="0 0 12 8"><path d="M1 1l5 5 5-5" fill="none" stroke="#444" stroke-width="1.4"/></svg></div>

  <h2 class="section-title" style="left:157px;top:1005px">ELECTRICAL INFORMATION</h2>
  <span class="label" style="left:156px;top:1045px">Main Breaker Size</span>
  <div class="select" style="left:278px;top:1039px;width:142px">Choose<svg width="12" height="8" viewBox="0 0 12 8"><path d="M1 1l5 5 5-5" fill="none" stroke="#444" stroke-width="1.4"/></svg></div>
  <span class="label" style="left:451px;top:1043px">Location</span>
  <div class="select" style="left:514px;top:1038px;width:152px">Choose<svg width="12" height="8" viewBox="0 0 12 8"><path d="M1 1l5 5 5-5" fill="none" stroke="#444" stroke-width="1.4"/></svg></div>
  <span class="label" style="left:156px;top:1080px">Main Panel Location</span>
  <div class="select" style="left:278px;top:1073px;width:142px">Choose<svg width="12" height="8" viewBox="0 0 12 8"><path d="M1 1l5 5 5-5" fill="none" stroke="#444" stroke-width="1.4"/></svg></div>
  <span class="label" style="left:433px;top:1078px">Sub Location</span>
  <div class="select" style="left:514px;top:1073px;width:152px">Choose<svg width="12" height="8" viewBox="0 0 12 8"><path d="M1 1l5 5 5-5" fill="none" stroke="#444" stroke-width="1.4"/></svg></div>
  <span class="label" style="left:156px;top:1114px">Inverter Location</span>
  <div class="select" style="left:282px;top:1110px;width:383px"><svg width="12" height="8" viewBox="0 0 12 8"><path d="M1 1l5 5 5-5" fill="none" stroke="#444" stroke-width="1.4"/></svg></div>

  <span class="label" style="left:742px;top:162px">Consultant</span>
  <div class="field" style="left:912px;top:158px;width:296px"></div>
  <span class="label" style="left:742px;top:193px">Phone</span>
  <div class="field" style="left:912px;top:190px;width:296px"></div>
  <span class="label" style="left:742px;top:225px">Date</span>
  <div class="field" style="left:912px;top:222px;width:296px"></div>
  <span class="label" style="left:742px;top:256px">Tentative Installation Date</span>
  <div class="field" style="left:912px;top:254px;width:296px"></div>

  <h2 class="section-title" style="left:742px;top:294px">SYSTEM DATE</h2>
  <span class="label" style="left:742px;top:329px">Total System Size (kW)</span>
  <div class="field" style="left:912px;top:322px;width:296px"></div>
  <span class="label" style="left:742px;top:360px">Panel Type</span>
  <div class="field" style="left:912px;top:354px;width:296px"></div>
  <span class="label" style="left:742px;top:392px">Is it ok with customer to mov vents/pipe/fans as needed?</span>
  <div class="select" style="left:1091px;top:386px;width:116px">Choose<svg width="12" height="8" viewBox="0 0 12 8"><path d="M1 1l5 5 5-5" fill="none" stroke="#444" stroke-width="1.4"/></svg></div>

  <table class="survey-table">
    <colgroup><col style="width:147px"><col style="width:63px"><col style="width:94px"><col style="width:89px"><col style="width:75px"></colgroup>
    <thead><tr><th class="group">ROOF MOUNT</th><th>Main</th><th>Add notes</th><th>Add notes</th><th>Add notes</th></tr></thead>
    <tbody>
      <tr><td class="row-label">Roof type</td><td></td><td></td><td></td><td></td></tr>
      <tr><td class="row-label">#of Layers</td><td></td><td></td><td></td><td></td></tr>
      <tr><td class="row-label">Artic Access?</td><td></td><td></td><td></td><td></td></tr>
      <tr><td class="row-label">Rafter Size</td><td></td><td></td><td></td><td></td></tr>
      <tr><td class="row-label">Rafter Spacing</td><td></td><td></td><td></td><td></td></tr>
      <tr><td class="row-label">Horizontal Span</td><td></td><td></td><td></td><td></td></tr>
      <tr><td class="row-label">Trench Length</td><td></td><td></td><td></td><td></td></tr>
      <tr><td class="row-label strong">GROUND MOUNT</td><td></td><td></td><td></td><td></td></tr>
      <tr><td class="row-label">Location of Array</td><td></td><td></td><td></td><td></td></tr>
      <tr><td class="row-label">Trench Length</td><td></td><td></td><td></td><td></td></tr>
    </tbody>
  </table>

  <h2 class="section-title" style="left:742px;top:842px">SPECIAL INSTRUCTIONS FROM HOMEOWNER</h2>
  <div class="field" style="left:742px;top:873px;width:465px"></div>
  <div class="field" style="left:742px;top:908px;width:466px"></div>

  <h2 class="section-title" style="left:741px;top:959px">MEASURE INFORMATION</h2>
  <span class="label" style="left:743px;top:990px">Do trees to be cut?</span>
  <div class="field" style="left:860px;top:985px;width:78px"></div>
  <span class="label" style="left:950px;top:990px">When?</span>
  <div class="field" style="left:997px;top:985px;width:69px"></div>
  <span class="note" style="left:1075px;top:989px">(New site survey will be required)</span>
  <span class="label" style="left:743px;top:1022px">Instruction for Measure / Installation Crew</span>
  <div class="field" style="left:744px;top:1051px;width:464px"></div>
  <div class="field" style="left:744px;top:1088px;width:464px"></div>

  <footer class="footer"></footer>
  <p class="copyright">© 2015 Company Name&nbsp; All right reserved&nbsp; Term of Use</p>
</div>
</body>
</html>
```